Music Festival Business Cards

The Lantern Gathering
Produced by Bramblewood Sound Collective LLC
New music festival in Arkansas.

Target Market(s)

18-35 year olds

Industry/Entity Type

Festival

Contact Information for Business Card

We are a 5-partner team producing a music festival in Arkansas. We need slick business cards, and I want them to be square.

Requirements
Must have
• I NEED THESE TO BE IN SQUARE SIZE - 2x2 or 2.5x2.5... please not regular size.
• I need www.lanternmeet.example as the link to website.

```html
<!DOCTYPE html>
<html lang="en">
<head>
<meta charset="utf-8">
<title>The Lantern Gathering — Square Business Cards</title>
<link href="https://fonts.googleapis.com/css2?family=Arimo:wght@400;700&display=swap" rel="stylesheet">
<style>
  :root {
    --stage: #2c2e31;
    --card-dark: #1d2226;
    --card-light: #ffffff;
    --accent: #45c3cf;
    --ink: #1a1a1a;
    --ink-soft: #2e2e2e;
  }
  * { box-sizing: border-box; margin: 0; padding: 0; }
  html, body {
    width: 1200px;
    height: 800px;
    overflow: hidden;
    background: var(--stage);
    font-family: "Arimo", Arial, sans-serif;
  }
  .stage {
    width: 1200px;
    height: 800px;
    display: flex;
    align-items: center;
    justify-content: center;
    gap: 80px;
  }
  .card {
    width: 420px;
    height: 420px;
    border-radius: 34px;
    overflow: hidden;
    position: relative;
    box-shadow: 0 18px 40px rgba(0,0,0,0.45);
  }

  /* Front */
  .card-front {
    background: var(--card-dark);
    display: flex;
    flex-direction: column;
    align-items: center;
    justify-content: center;
    gap: 26px;
  }
  .brand-dot {
    width: 22px;
    height: 22px;
    border-radius: 50%;
    background: var(--accent);
  }
  .brand-name {
    color: var(--accent);
    font-weight: 700;
    font-size: 34px;
    letter-spacing: 3px;
    text-transform: uppercase;
    text-align: center;
    line-height: 1.2;
  }

  /* Back */
  .card-back {
    background: var(--card-light);
  }
  .contact {
    position: absolute;
    top: 44px;
    right: 40px;
    width: 300px;
    text-align: right;
    color: var(--ink-soft);
  }
  .person-name {
    font-weight: 700;
    font-size: 22px;
    letter-spacing: 1px;
    color: var(--ink);
    text-transform: uppercase;
  }
  .person-role {
    font-size: 16px;
    color: var(--accent);
    margin-top: 2px;
  }
  .contact-row {
    border-top: 1px solid var(--accent);
    margin-top: 12px;
    padding-top: 8px;
  }
  .contact-label {
    font-size: 12px;
    font-weight: 700;
    color: var(--accent);
  }
  .contact-value {
    font-size: 17px;
    line-height: 1.3;
  }
  .web-band {
    position: absolute;
    left: 0;
    right: 0;
    bottom: 0;
    height: 62px;
    background: var(--accent);
    border-top: 4px solid var(--card-light);
    box-shadow: 0 -3px 0 var(--ink);
    display: flex;
    align-items: center;
    justify-content: center;
  }
  .web-address {
    font-size: 18px;
    color: var(--ink);
    letter-spacing: 0.5px;
  }
</style>
</head>
<body>
  <main class="stage">
    <section class="card card-front" aria-label="Card front">
      <span class="brand-dot" aria-hidden="true"></span>
      <h1 class="brand-name">The Lantern<br>Gathering</h1>
    </section>

    <section class="card card-back" aria-label="Card back">
      <div class="contact">
        <p class="person-name">Rowan Hale</p>
        <p class="person-role">Manager</p>
        <div class="contact-row">
          <p class="contact-label">Phone</p>
          <p class="contact-value">(555) 014-2290</p>
        </div>
        <div class="contact-row">
          <p class="contact-label">E-mail</p>
          <p class="contact-value">hello@lanternmeet.example</p>
        </div>
        <div class="contact-row">
          <p class="contact-value">PO BOX 48 Lantern Lane<br>Fayetteville, Arkansas</p>
        </div>
      </div>
      <div class="web-band">
        <p class="web-address">www.lanternmeet.example</p>
      </div>
    </section>
  </main>
</body>
</html>
```